Flyer promoting printing services to bars and restaurants

Small print company specialising in print for pubs, bard and restaurants looking for someone to design a flyer promoting our services which will be mailed to a database of potential customers. We have the text but need this putting into a nice design. The text is attached.

Ideally we would want separate versions - one for pubs / bars and another for restaurants.

Target Market(s)

Bars, pubs and restaurants

```html
<!DOCTYPE html>
<html lang="en">
<head>
<meta charset="utf-8">
<title>Brantwood Print – Printing services for pubs, bars and restaurants</title>
<link href="https://fonts.googleapis.com/css2?family=Cabin:ital,wght@0,400;0,600;0,700;1,400&display=swap" rel="stylesheet">
<style>
  :root {
    --red: #e8383d;
    --red-dark: #c42a2f;
    --navy: #1e3f72;
    --ink: #1b1b1b;
    --grey: #555;
    --white: #ffffff;
    --blush: #d6aea5;
    --blue: #1f4a8a;
    --yellow: #ffe600;
    --orange: #f39a1e;
    --green: #10a048;
  }
  html, body { margin: 0; padding: 0; overflow: hidden; }
  body { width: 848px; height: 1200px; }
  .flyer {
    position: relative;
    width: 848px;
    height: 1200px;
    overflow: hidden;
    font-family: "Cabin", sans-serif;
    color: var(--ink);
    background: linear-gradient(180deg, #ffffff 0%, #ffffff 48%, #e9cfc8 70%, var(--blush) 100%);
  }
  .mosaic-backdrop {
    position: absolute;
    left: 0; top: 0;
    width: 848px; height: 560px;
    background:
      radial-gradient(ellipse 300px 300px at 424px 210px, #ffffff 0%, #ffffff 78%, rgba(255,255,255,0) 100%),
      linear-gradient(90deg, #f2a9c4 0%, #b9dcef 18%, rgba(255,255,255,0) 40%, rgba(255,255,255,0) 60%, #f7c6a8 82%, #a9c8ee 100%);
    opacity: 0.85;
  }
  .brand {
    position: absolute;
    left: 0; right: 0; top: 42px;
    text-align: center;
  }
  .brand-dot {
    display: block;
    width: 84px; height: 84px;
    margin: 0 auto 34px;
    border-radius: 50%;
    background: var(--red);
  }
  .brand-name {
    margin: 0;
    font-family: "Cabin", sans-serif;
    font-weight: 600;
    font-size: 34px;
    color: var(--ink);
    line-height: 1;
  }
  .brand-tagline {
    margin: 12px 0 0;
    font-size: 18px;
    color: var(--grey);
  }
  .bottles {
    position: absolute;
    left: 272px; top: 262px;
    width: 304px; height: 118px;
    border-radius: 10px;
    background: linear-gradient(90deg, #34c5e0 0%, #3cb54a 20%, #d8df2a 40%, #e51f25 60%, #c42ea8 80%, #1d3aa8 100%);
    opacity: 0.9;
  }
  .ribbon {
    position: absolute;
    left: 44px; top: 408px;
    width: 760px; height: 96px;
  }
  .ribbon svg { position: absolute; left: 0; top: 0; }
  .ribbon-title {
    position: absolute;
    left: 0; right: 0; top: 4px;
    margin: 0;
    text-align: center;
    color: var(--white);
    font-weight: 600;
    font-size: 40px;
    line-height: 43px;
    letter-spacing: -0.3px;
  }
  .services {
    position: absolute;
    left: 44px; top: 566px;
    width: 392px;
  }
  .services-heading {
    margin: 0 0 14px 30px;
    color: var(--red);
    font-weight: 600;
    font-size: 29px;
    line-height: 27px;
  }
  .service-list { list-style: none; margin: 0; padding: 0; }
  .service-list li {
    position: relative;
    padding-left: 30px;
    font-size: 18.5px;
    line-height: 28.6px;
    text-transform: uppercase;
  }
  .service-list li::before {
    content: "";
    position: absolute;
    left: 0; top: 6px;
    width: 16px; height: 16px;
    background: var(--bullet);
  }
  .contact {
    position: absolute;
    left: 0; top: 1012px;
    width: 345px; height: 132px;
    padding: 10px 0 0 74px;
    background: var(--navy);
    color: var(--white);
    font-style: normal;
    font-size: 17px;
    line-height: 18.5px;
  }
  .contact p { margin: 0 0 12px; }
  .contact strong { font-weight: 700; }
  .intro {
    position: absolute;
    left: 452px; top: 574px;
    width: 345px;
    font-size: 19.6px;
    line-height: 25.6px;
  }
  .intro p { margin: 0; }
  .intro .justified { text-align: justify; }
  .highlight { color: var(--red); }
  .highlight-strong { color: var(--red); font-weight: 700; }
  .small-note {
    position: absolute;
    left: 452px; top: 1102px;
    width: 345px;
    margin: 0;
    text-align: center;
    font-style: italic;
    font-size: 16px;
    color: #333;
  }
</style>
</head>
<body>
<div class="flyer">
  <div class="mosaic-backdrop" role="img" aria-label="Decorative burst of overlapping coloured squares radiating around a white circle"></div>

  <header class="brand">
    <span class="brand-dot"></span>
    <h1 class="brand-name">Brantwood Print</h1>
    <p class="brand-tagline">Print that makes its mark</p>
  </header>

  <div class="bottles" role="img" aria-label="Row of six coloured glass bottles: cyan, green, yellow, red, magenta and blue"></div>

  <div class="ribbon">
    <svg width="760" height="96" viewBox="0 0 760 96" aria-hidden="true">
      <polygon points="0,90 44,84 60,60 60,96" fill="#c42a2f"/>
      <polygon points="760,90 716,84 700,60 700,96" fill="#c42a2f"/>
      <polygon points="10,92 56,36 56,96" fill="#e8383d"/>
      <polygon points="750,92 704,36 704,96" fill="#e8383d"/>
      <rect x="56" y="2" width="648" height="92" fill="#e8383d"/>
    </svg>
    <h2 class="ribbon-title">PRINTING SERVICES FOR<br>PUBS, BARS AND RESTAURANTS</h2>
  </div>

  <section class="services">
    <h3 class="services-heading">SOME OF THE PRINTING<br>SERVICES WE PROVIDE:</h3>
    <ul class="service-list">
      <li style="--bullet: var(--blue)">Posters &amp; banners: any size, indoor<br>or outdoor, no minimum quantity,<br>fast turnaround</li>
      <li style="--bullet: var(--red)">Branded / personalised clothing:<br>T-shirts, polo-shirts, aprons,<br>chefswear</li>
      <li style="--bullet: var(--yellow)">Menus: printed sheets to insert<br>into menu books or free standing<br>folded menus. All formats</li>
      <li style="--bullet: var(--orange)">Multi-part NCR order pads (no<br>carbon required) and note pads</li>
      <li style="--bullet: var(--green)">Table talkers / tent cards &nbsp;Flyers<br>and leaflets</li>
    </ul>
  </section>

  <address class="contact">
    <p>Contact : Marcus on &nbsp;<strong>01632 960415</strong><br>or email marcus@brantwoodprint.uk</p>
    <p>Brantwood Print, Unit 4 Falcon Court,<br>Mill Lane, Ashby Green, Essex, CM9 2QT</p>
    <p>www.brantwoodprint.uk</p>
  </address>

  <section class="intro">
    <p class="justified">Introducing Brantwood Print, an Essex based printing company that prides itself on taking the <span class="highlight">personalised approach to our customer.</span> We focus on specific sectors to ensure that we meet the requirements of our customers. Pubs and restaurants are one of the sectors in which we have a great deal of experience of providing print for.</p>
    <p>Whatever your requirements, Brantwood Print offer a fast friendly service using the latest printing technology to produce <span class="highlight-strong">high quality print.</span></p>
    <p>We also have our own in-house design studio and can help out with any design work if required.</p>
    <p>Please don’t hesitate to get in touch and we would be happy to help. We never turn down an excuse to visit the pub!</p>
  </section>

  <p class="small-note">No minimum quantity on any order</p>
</div>
</body>
</html>
```